Label for water can - new packaging of luxury Velmora Silk water

We create water can - handy disposable metal packaging that can be closed with a cap and used for a long time. We want to stand out, look different from typical other water brands.

It is a product that the clients impulsively buys because the design attracts them. They want to take it out of their bag, they want to give it to their clients. They want to have the ORA with them all the time.

The packaging is great for kids, but we don't design product for kids. We create a tasteful luxury UNISEX design for parents who want to buy it for themselves and give it to their children at the same time.

The client will buy our product for the first time because of the design and type of packaging, the taste will make him a loyal client.

Most of water brands are generally tuned in white-blue style.

They all use images of nature, water.

We want to be different.

We are angelic water.

Minimalism describes us.

An important part of the Velmora Silk concept is wood (our glass barrel comes in a wooden case).

Our clients like gold and silver color.

The product name is ORA. And that word has a double meaning.
WATER ORA MAKE YOU HAPPY…
WATER ORA HELP YOU…
WATER ORA ENRICHE YOU…
We will play with it in future communication.

Target Market(s)

Luxury water bevarage

Font styles to use
Other font styles liked:
• Seravek, Gotham, Playfair Display

Colors
0094D4
00A9DD
6FCCEA
C7EBF8
E9F6FB

Requirements
Must have
• Packaging supports impulsive shopping, is untraditional and unisex
Should not have
• Elements traditional for water packaging

```html
<!DOCTYPE html>
<html lang="en">
<head>
<meta charset="utf-8">
<title>Velmora Silk — ORA label</title>
<link rel="stylesheet" href="https://fonts.googleapis.com/css2?family=Cinzel:wght@400;500&family=Playfair+Display:wght@400;500&display=swap">
<style>
  :root {
    --stage: #f7f7f7;
    --label-top: #ffffff;
    --label-mid: #fbfbf4;
    --label-base: #f3e6da;
    --ink: #1c2431;
    --brand-ink: #17212e;
    --halo: #00a9dd;
    --gold-light: #f6e39a;
    --gold: #d9b23c;
    --gold-deep: #a9801c;
    --wing-light: #fbe98a;
    --wing: #f0c93a;
    --wing-deep: #d99a1e;
  }

  * { box-sizing: border-box; margin: 0; padding: 0; }

  html, body {
    width: 1200px;
    height: 900px;
    overflow: hidden;
    background: var(--stage);
  }

  .canvas {
    width: 1200px;
    height: 900px;
    display: flex;
    align-items: center;
    justify-content: center;
  }

  .label {
    width: 560px;
    height: 840px;
    background: linear-gradient(180deg,
      var(--label-top) 0%,
      var(--label-top) 45%,
      var(--label-mid) 70%,
      var(--label-base) 100%);
    display: flex;
    flex-direction: column;
    align-items: center;
    padding-top: 64px;
  }

  .brand {
    display: flex;
    align-items: center;
    gap: 12px;
    font-family: "Playfair Display", Georgia, serif;
    font-weight: 400;
    font-size: 40px;
    color: var(--brand-ink);
    letter-spacing: 0.5px;
  }

  .brand-dot {
    width: 14px;
    height: 14px;
    border-radius: 50%;
    background: var(--halo);
  }

  .wings-art {
    margin-top: 30px;
    width: 400px;
    height: 330px;
    border-radius: 50% 50% 46% 46% / 42% 42% 58% 58%;
    background: radial-gradient(ellipse at 50% 45%,
      var(--wing-light) 0%,
      var(--wing) 55%,
      var(--wing-deep) 100%);
    opacity: 0.85;
  }

  .product-name {
    margin-top: 22px;
    font-family: "Cinzel", "Times New Roman", serif;
    font-weight: 400;
    font-size: 136px;
    line-height: 1;
    letter-spacing: 2px;
    background: linear-gradient(180deg,
      var(--gold-light) 0%,
      var(--gold) 45%,
      var(--gold-deep) 80%,
      var(--gold) 100%);
    -webkit-background-clip: text;
    background-clip: text;
    color: transparent;
  }

  .claims {
    margin-top: 34px;
    list-style: none;
    display: flex;
    flex-direction: column;
    align-items: center;
    font-family: "Playfair Display", Georgia, serif;
    font-size: 23px;
    color: var(--ink);
  }

  .claim-divider {
    width: 24px;
    height: 2px;
    background: var(--gold);
    margin: 10px 0 12px;
  }
</style>
</head>
<body>
  <main class="canvas">
    <section class="label">
      <header class="brand">
        <span>Velmora Silk</span>
        <span class="brand-dot"></span>
      </header>

      <div class="wings-art" role="img" aria-label="Golden liquid splash shaped like butterfly wings"></div>

      <h1 class="product-name">ORA</h1>

      <ul class="claims">
        <li>Alkaline PH</li>
        <li class="claim-divider" aria-hidden="true"></li>
        <li>Low In Minerals</li>
        <li class="claim-divider" aria-hidden="true"></li>
        <li>Icelandic Glacier Water</li>
      </ul>
    </section>
  </main>
</body>
</html>
```